Consulting company needs website design

We need a simple, static website design for our consulting company. We are looking for a general design of the look and feel of the website. Initially, it will have these pages:
- Home
- About us
- Services
- Contact us
We have our own logo which I have attached to the brief.

We are looking for a simple website, with white background and the use of gray (darker) as the main theme. Simple fonts. The website should be responsive so it an be easily red in mobile devices.

As part of the project, we will need to receive at least the following items:
- Individual files with sample text to support the pages outlined above
- Necessary CSS files

Our current website is here: http://www.marlowvane.co/

Here are some examples of other website we like to be used as guideline:
- http://www.tornaviamundo.com/
-

Target Market(s)

Individuals and companies looking to hire our company to provide consulting services.

Industry/Entity Type

It Company

Coding

Coded - Design and coding required

Number of Pages Required

4 page

Font styles to use
Sans Serif

Requirements
Must have
• Main page should have the ability to embed Chirply feed into it.
• We prefer the design to use gray tones.

```html
<!DOCTYPE html>
<html lang="en">
<head>
<meta charset="utf-8">
<title>Marlowvane Group – Consulting</title>
<link href="https://fonts.googleapis.com/css2?family=Open+Sans:wght@400;600;700;800&display=swap" rel="stylesheet">
<style>
:root{
  --ink:#333;
  --text:#555;
  --muted:#777;
  --band:#444;
  --band-dark:#3a3a3a;
  --panel:#f0f0f0;
  --line:#ddd;
  --white:#fff;
  --icon:#6b6b6b;
}
*{box-sizing:border-box;margin:0;padding:0}
html,body{width:1200px;height:2384px;overflow:hidden;background:var(--white)}
body{font-family:"Open Sans",Arial,sans-serif;color:var(--text);position:relative}
.abs{position:absolute}

/* header */
.site-header{position:absolute;left:0;top:0;width:1200px;height:116px;background:var(--white)}
.brand{position:absolute;left:78px;top:26px;display:flex;align-items:center;gap:16px}
.brand-mark{width:70px;height:70px;border-radius:50%;border:3px solid #999}
.brand-name{font-weight:700;font-size:22px;line-height:27px;color:#555;letter-spacing:.5px;text-transform:uppercase}
.social{position:absolute;display:flex;gap:6px}
.social span{width:30px;height:30px;border-radius:50%;background:#666;display:block}
.site-header .social{left:808px;top:47px}
.search{position:absolute;left:1102px;top:50px}

/* nav */
.main-nav{position:absolute;left:0;top:116px;width:1200px;height:51px;background:var(--band);display:flex;align-items:center;padding-left:76px}
.main-nav a{color:var(--white);text-decoration:none;font-size:13px;font-weight:600;margin-right:48px;text-transform:uppercase}

/* hero */
.hero{position:absolute;left:0;top:167px;width:1200px;height:490px;background:linear-gradient(100deg,#6e655d 0%,#8a8078 35%,#a8a39d 60%,#c9c4bb 100%)}
.hero h1{position:absolute;left:78px;top:122px;font-size:56px;line-height:60px;font-weight:800;color:var(--white);text-transform:uppercase}
.hero p{position:absolute;left:78px;top:240px;font-size:33px;font-weight:700;color:var(--white)}
.dots{position:absolute;left:75px;top:308px;display:flex;gap:6px}
.dots span{width:17px;height:17px;border-radius:50%;background:#bbb}
.dots span:first-child{background:var(--white)}

/* welcome */
.welcome h2{position:absolute;left:75px;top:704px;font-size:23px;font-weight:400;color:var(--ink);text-transform:uppercase}
.welcome p{position:absolute;left:75px;top:745px;width:605px;font-size:13px;line-height:24px;color:var(--text)}
.btn{position:absolute;left:75px;top:891px;width:151px;height:43px;background:#5a5a5a;border:1px solid #444;color:var(--white);font-size:12px;font-weight:700;display:flex;align-items:center;justify-content:center;text-transform:uppercase}
.welcome-photo{position:absolute;left:704px;top:710px;width:423px;height:225px;background:linear-gradient(120deg,#d8d4cc,#8a8580 55%,#3e4450)}

/* services */
.services{position:absolute;left:0;top:985px;width:1200px;height:468px;background:var(--band-dark)}
.services h2{position:absolute;top:45px;width:100%;text-align:center;color:var(--white);font-size:22px;font-weight:400;text-transform:uppercase}
.services .lead{position:absolute;top:88px;width:100%;text-align:center;color:var(--white);font-size:13px}
.service{position:absolute;top:148px;width:250px;text-align:center;color:var(--white)}
.service svg{display:block;margin:0 auto}
.service h3{font-size:19px;font-weight:700;margin-top:18px;letter-spacing:.3px}
.service p{font-size:13px;line-height:24px;margin-top:6px;padding:0 4px}

/* panels */
.panel{position:absolute;top:1500px;width:512px;height:387px;border:1px solid var(--line);background:var(--white)}
.panel-head{height:58px;background:var(--panel);border-bottom:1px solid var(--line);display:flex;align-items:center;justify-content:space-between;padding:0 18px 0 20px}
.panel-head h2{font-size:21px;font-weight:400;color:var(--ink);text-transform:uppercase}
.tag-btn{height:31px;padding:0 16px;border:1px solid #ccc;background:#f7f7f7;font-size:11px;font-weight:700;color:#555;display:flex;align-items:center;gap:6px;text-transform:uppercase}
.news-item{position:absolute;left:20px;width:465px;display:flex;gap:20px}
.news-thumb{width:156px;height:106px;background:linear-gradient(135deg,#dfe6ee,#9fb2c6 55%,#6f8aa5);flex:none}
.news-item h4{font-size:14px;font-weight:700;color:#555;margin-top:2px}
.news-item p{font-size:13px;line-height:23px;color:var(--text);margin-top:4px}
.news-item b{color:#444}
.rule{position:absolute;height:1px;background:var(--line)}
.tweet{position:absolute;left:20px;width:462px;display:flex;gap:22px}
.avatar{width:67px;height:67px;border:1px solid #ccc;flex:none;display:flex;align-items:center;justify-content:center}
.avatar span{width:38px;height:38px;border-radius:50%;border:2px solid #aaa}
.tweet h4{font-size:14px;font-weight:700;color:#555}
.tweet h4 small{font-size:12px;font-weight:400;color:#666}
.tweet p{font-size:12px;line-height:22px;color:#555}
.scroll{position:absolute;left:495px;top:92px;width:6px;height:40px;background:#bbb;border-radius:2px}

/* clients */
.clients{position:absolute;left:0;top:1922px;width:1200px;height:238px;background:#f2f2f2}
.clients h2{position:absolute;top:34px;width:100%;text-align:center;font-size:22px;font-weight:400;color:var(--ink);text-transform:uppercase}
.clients .lead{position:absolute;top:78px;width:100%;text-align:center;font-size:13px;color:var(--text)}
.client-row{position:absolute;left:78px;top:140px;width:1050px;display:flex;justify-content:space-between;align-items:center}
.client{display:flex;align-items:center;gap:10px;font-size:26px;font-weight:600;color:#6a6a6a}
.client i{display:block;width:34px;height:34px;border-radius:50%;background:#8a8a8a}

/* footer */
.site-footer{position:absolute;left:0;top:2160px;width:1200px;height:224px;background:var(--band)}
.foot-nav{position:absolute;left:0;top:34px;width:100%;display:flex;justify-content:center;gap:50px}
.foot-nav a{color:var(--white);text-decoration:none;font-size:12px;text-transform:uppercase}
.foot-line{position:absolute;left:78px;top:80px;width:1047px;height:1px;background:#5c5c5c}
.foot-brand{position:absolute;left:78px;top:103px;display:flex;align-items:center;gap:14px}
.foot-brand .brand-mark{width:44px;height:44px;border:2px solid var(--white)}
.foot-brand .brand-name{font-size:13px;line-height:17px;color:var(--white)}
.legal{position:absolute;left:87px;top:162px;font-size:11px;line-height:21px;color:#aaa}
.connect{position:absolute;left:960px;top:112px;color:var(--white);font-size:14px;font-weight:600;text-transform:uppercase}
.site-footer .social{left:960px;top:143px}
.site-footer .social span{background:#bbb;width:28px;height:28px}
</style>
</head>
<body>

<header class="site-header">
  <div class="brand"><span class="brand-mark"></span><div class="brand-name">Marlowvane<br>Group</div></div>
  <div class="social"><span></span><span></span><span></span><span></span><span></span></div>
  <svg class="search" width="20" height="20" viewBox="0 0 20 20"><circle cx="8" cy="8" r="6" fill="none" stroke="#444" stroke-width="2.6"/><line x1="12.5" y1="12.5" x2="18" y2="18" stroke="#444" stroke-width="3" stroke-linecap="round"/></svg>
</header>

<nav class="main-nav">
  <a href="#">Home</a><a href="#">Who we are</a><a href="#">What we do</a><a href="#">Our services</a><a href="#">Latest news</a><a href="#">Clients</a><a href="#">Careers</a><a href="#">Blog</a><a href="#">Contact us</a>
</nav>

<section class="hero" role="img" aria-label="Laptop on an office desk with a cloud software diagram on screen, city skyline in the background">
  <h1>Welcome to<br>Marlowvane Group</h1>
  <p>We are a Consulting Company</p>
  <div class="dots"><span></span><span></span><span></span><span></span></div>
</section>

<section class="welcome">
  <h2>Welcome to our website</h2>
  <p>Aliquam molestie, mi et imperdiet euismod, dui purus auctor tellus, et interdum lacus lectus et ante. Sed accumsan sollicitudin sapien, sit amet adipiscing turpis gravida ac. In congue, neque ac lobortis volutpat, libero mauris varius mi, vitae suscipit ipsum ligula vitae risus.<br>Duis aliquam nibh a dui iaculis viverra id a velit. Vivamus egestas risus in magna varius commodo etiam pretium porttitor lectus, vel ornare neque porta volutpat.</p>
  <div class="btn">Read more</div>
  <div class="welcome-photo" role="img" aria-label="Two businessmen reviewing a tablet at an office desk"></div>
</section>

<section class="services">
  <h2>What we do</h2>
  <p class="lead">Aliquam molestie, mi et imperdiet euismod, dui purus auctor tellus, et interdum lacus lectus et ante.</p>

  <div class="service" style="left:70px">
    <svg width="120" height="120" viewBox="0 0 120 120"><polygon points="35,2 85,2 118,35 118,85 85,118 35,118 2,85 2,35" fill="#fff"/><g fill="#666"><circle cx="60" cy="38" r="7"/><rect x="53" y="46" width="14" height="5"/><path d="M54 51h12l3 24H51z"/><rect x="46" y="75" width="28" height="7" rx="2"/></g></svg>
    <h3>Strategy</h3>
    <p>Duis aliquam nibh a dui iaculis viverra id a velit. Vivamus egestas risus in magna varius commodo.</p>
  </div>
  <div class="service" style="left:338px">
    <svg width="120" height="120" viewBox="0 0 120 120"><polygon points="35,2 85,2 118,35 118,85 85,118 35,118 2,85 2,35" fill="#fff"/><g fill="#666"><circle cx="60" cy="52" r="20"/><rect x="52" y="72" width="16" height="6"/><rect x="53" y="80" width="14" height="4"/><rect x="55" y="86" width="10" height="4"/></g><text x="60" y="60" text-anchor="middle" font-family="Open Sans,sans-serif" font-weight="700" font-size="22" fill="#fff">$</text></svg>
    <h3>Finance</h3>
    <p>Duis aliquam nibh a dui iaculis viverra id a velit. Vivamus egestas risus in magna varius commodo.</p>
  </div>
  <div class="service" style="left:611px">
    <svg width="120" height="120" viewBox="0 0 120 120"><polygon points="35,2 85,2 118,35 118,85 85,118 35,118 2,85 2,35" fill="#fff"/><g fill="none" stroke="#666" stroke-width="3"><rect x="33" y="32" width="40" height="50"/><line x1="40" y1="44" x2="66" y2="44"/><line x1="40" y1="54" x2="60" y2="54"/><circle cx="72" cy="74" r="15" fill="#fff"/><polyline points="72,66 72,75 79,78"/></g></svg>
    <h3>Project Management</h3>
    <p>Duis aliquam nibh a dui iaculis viverra id a velit. Vivamus egestas risus in magna varius commodo.</p>
  </div>
  <div class="service" style="left:880px">
    <svg width="120" height="120" viewBox="0 0 120 120"><polygon points="35,2 85,2 118,35 118,85 85,118 35,118 2,85 2,35" fill="#fff"/><g fill="#666"><rect x="34" y="62" width="7" height="16"/><rect x="45" y="56" width="7" height="22"/><rect x="56" y="60" width="7" height="18"/><rect x="67" y="50" width="7" height="28"/><rect x="78" y="44" width="7" height="34"/><rect x="30" y="80" width="60" height="3"/></g><polyline points="34,55 48,44 60,50 84,34" fill="none" stroke="#666" stroke-width="3"/></svg>
    <h3>Analytics</h3>
    <p>Duis aliquam nibh a dui iaculis viverra id a velit. Vivamus egestas risus in magna varius commodo.</p>
  </div>
</section>

<section class="panel" style="left:75px">
  <div class="panel-head"><h2>Latest New</h2><div class="tag-btn">Read all</div></div>
  <div class="news-item" style="top:92px">
    <div class="news-thumb" role="img" aria-label="Hands reviewing financial charts on paper"></div>
    <div><h4>JUL 18, 2016</h4><p>Sed accumsan sollicitudin sapien, sit amet adipiscing turpis gravida ac. In congue, neque ac lobortis volutpat, libero mauris varius mi, vitae suscipit..<b>Read More</b></p></div>
  </div>
  <div class="rule" style="left:20px;top:223px;width:465px"></div>
  <div class="news-item" style="top:247px">
    <div class="news-thumb" role="img" aria-label="Business report with graphs on a desk"></div>
    <div><h4>JUL 18, 2016</h4><p>Sed accumsan sollicitudin sapien, sit amet adipiscing turpis gravida ac. In congue, neque ac lobortis volutpat, libero mauris varius mi, vitae suscipit..<b>Read More</b></p></div>
  </div>
</section>

<section class="panel" style="left:615px">
  <div class="panel-head"><h2>Chirply Feeds</h2><div class="tag-btn"><svg width="14" height="11" viewBox="0 0 14 11"><circle cx="5" cy="3" r="3" fill="#4a7fb5"/><path d="M0 11c0-4 10-4 10 0z" fill="#4a7fb5"/><path d="M11 2v6M8 5h6" stroke="#4a7fb5" stroke-width="1.6"/></svg>Follow</div></div>
  <div class="scroll"></div>
  <div class="tweet" style="top:92px"><div class="avatar"><span></span></div><div><h4>Marlowvane Group <small>@MarlowvaneGroup&nbsp; Jul 14</small></h4><p>Great insights about <b>#data</b> and <b>#analytics</b> at the Halden<br>CDO/Information Quality Symposium...</p></div></div>
  <div class="rule" style="left:20px;top:176px;width:462px"></div>
  <div class="tweet" style="top:192px"><div class="avatar"><span></span></div><div><h4>Marlowvane Group <small>@MarlowvaneGroup&nbsp; Jul 14</small></h4><p>Great insights about <b>#data</b> and <b>#analytics</b> at the Halden<br>CDO/Information Quality Symposium...</p></div></div>
  <div class="rule" style="left:20px;top:276px;width:462px"></div>
  <div class="tweet" style="top:292px"><div class="avatar"><span></span></div><div><h4>Marlowvane Group <small>@MarlowvaneGroup&nbsp; Jul 14</small></h4><p>Great insights about <b>#data</b> and <b>#analytics</b> at the Halden<br>CDO/Information Quality Symposium...</p></div></div>
</section>

<section class="clients">
  <h2>Our Clients</h2>
  <p class="lead">Aliquam molestie, mi et imperdiet euismod, dui purus auctor tellus, et interdum lacus lectus et ante.</p>
  <div class="client-row">
    <div class="client">Corvela Partners</div>
    <div class="client"><i></i>Brantley &amp; Oake</div>
    <div class="client">Tessaro Research</div>
    <div class="client">Quillmark</div>
    <div class="client">Ostrand &amp; Co</div>
  </div>
</section>

<footer class="site-footer">
  <nav class="foot-nav">
    <a href="#">Home</a><a href="#">Who we are</a><a href="#">What we do</a><a href="#">Our services</a><a href="#">Latest news</a><a href="#">Clients</a><a href="#">Careers</a><a href="#">Blog</a><a href="#">Contact us</a>
  </nav>
  <div class="foot-line"></div>
  <div class="foot-brand"><span class="brand-mark"></span><div class="brand-name">Marlowvane<br>Group</div></div>
  <div class="legal">Copyright © 2016. Company Name. All Right Reserved<br>Terms of Services &nbsp;|&nbsp; Privacy Policy</div>
  <div class="connect">Connect us</div>
  <div class="social"><span></span><span></span><span></span><span></span><span></span></div>
</footer>

</body>
</html>
```